trading data display webpage

We have build a rough wireframe of the two webpages that we want to display .The two wireframes are attached as a pdf document.
there will be login page. after login , the user will see the index page. that is the first page of the wireframe.

what we are displaying is essentially spread data. we are taking the difference in prices are two places and displaying the data. some calculations are done and is shown in the grid.

below the grid we show the behaviour on a graph. we will use bubble chart. I did not find a sample, hence have thrown in a placeholder.

this is time series data ( changes daily) and hence we need to check the behaviour.

the second wire frame shows how the user will choose the source price points and the destination price points.
we are talking here of natural gas prices hence the reference to source prices and destination prices.

you need to design the page/ pages such that the end-user loves it and is easy to use. the intent here is easy to use and easy to understand.
this will be responsive webpage since the end user will check it out on a tablet or a smartphone.

so if possible tell us how the navigation bar, the button bar, etc should fall when the screen size decreases.

I have uploaded 2 files. one is the wireframe ( pdf document) and second is the logo file.

please also let us know where to place the logo.

Target Market(s)

the target market is traders and data analyst

Industry/Entity Type

Build

Colors

Designer to choose colors to be used in the design.

Requirements
Must have
• 1. design for the web.
2. but think how the design will look when the screen size decreases.
3. tell if possible what screen components to keep and what to hide.

```html
<!DOCTYPE html>
<html lang="en">
<head>
<meta charset="utf-8">
<title>GasSpread – Spread Dashboard</title>
<link rel="stylesheet" href="https://fonts.googleapis.com/css2?family=Questrial&display=swap">
<style>
  :root {
    --orange: #f26522;
    --orange-soft: #f7931e;
    --green: #8dc63f;
    --blue: #0054a6;
    --blue-light: #cfe2f3;
    --grey-dot: #a7a9ac;
    --ink: #1a1a1a;
    --muted: #555;
    --rule: #cfcfcf;
    --header-top: #ffffff;
    --header-bottom: #d9d9d9;
    --tab-grey: #e3e3e3;
  }
  html, body {
    margin: 0;
    width: 1200px;
    height: 2790px;
    overflow: hidden;
    background: #fff;
  }
  .page {
    position: relative;
    width: 320px;
    height: 744px;
    transform: scale(3.75);
    transform-origin: 0 0;
    font-family: "Questrial", "Century Gothic", sans-serif;
    color: var(--ink);
  }
  .masthead {
    position: absolute; left: 0; top: 0; width: 320px; height: 139px;
    background: linear-gradient(#ffffff 0%, #e6e6e6 55%, #ffffff 56%, #d4d4d4 100%);
  }
  .masthead .top {
    position: absolute; left: 0; top: 0; width: 320px; height: 83px;
    background: linear-gradient(var(--header-top), var(--header-bottom));
  }
  .masthead .band-orange {
    position: absolute; left: 0; top: 83px; width: 320px; height: 7px; background: var(--orange);
  }
  .masthead .band-blue {
    position: absolute; left: 0; top: 90px; width: 320px; height: 3px; background: var(--blue);
  }
  .masthead .lower {
    position: absolute; left: 0; top: 93px; width: 320px; height: 46px;
    background: linear-gradient(#ffffff, #d8d8d8);
  }
  .brand {
    position: absolute; left: 20px; top: 34px;
    display: flex; align-items: center; gap: 6px;
    font-size: 17px; color: var(--blue);
  }
  .brand .dot {
    width: 14px; height: 14px; border-radius: 50%; background: var(--orange);
  }
  .region-tabs {
    position: absolute; top: 116px; left: 52px; display: flex; gap: 4px;
  }
  .region-tabs span {
    display: block; height: 23px; line-height: 25px; text-align: center;
    font-size: 14px; border-radius: 6px 6px 0 0; background: var(--tab-grey); color: #222;
  }
  .region-tabs .active { width: 68px; background: var(--orange); color: #fff; }
  .region-tabs .t2 { width: 67px; }
  .region-tabs .t3 { width: 66px; }
  .filters { position: absolute; left: 18px; top: 148px; font-size: 13px; }
  .filters .label { height: 22px; line-height: 22px; }
  .filters .options { height: 22px; line-height: 22px; color: var(--orange); word-spacing: 2px; }
  .filters .options .sel { color: var(--green); }
  .filters .options .sep { margin: 0 9px; }
  .sort { font-size: 9px; vertical-align: 1px; letter-spacing: -1px; }
  .expand { display: flex; align-items: center; gap: 10px; }
  .rule { position: absolute; left: 16px; width: 272px; height: 1px; background: var(--rule); }
  .chart-title { position: absolute; left: 0; width: 320px; text-align: center; font-size: 13px; }
  .plot { position: absolute; left: 0; }
  .plot text { font-family: "Questrial", "Century Gothic", sans-serif; }
  .footer {
    position: absolute; left: 0; top: 671px; width: 320px; text-align: center;
    font-size: 10px; line-height: 13px; color: var(--muted);
  }
</style>
</head>
<body>
<div class="page">
  <header class="masthead">
    <div class="top"></div>
    <div class="band-orange"></div>
    <div class="band-blue"></div>
    <div class="lower"></div>
    <div class="brand"><span class="dot"></span>GasSpread</div>
    <nav class="region-tabs">
      <span class="active">East</span>
      <span class="t2">Central</span>
      <span class="t3">West</span>
    </nav>
  </header>

  <section class="filters">
    <div class="label">Source Indices <span class="sort">▲<br></span></div>
    <div class="options"><span class="sel">5 days</span><span class="sep">|</span>7 days<span class="sep">|</span>18 days</div>
    <div class="label">Destination Indices <span class="sort">▲</span></div>
    <div class="options"><span class="sel">Month</span><span class="sep">|</span>Year</div>
    <div class="label expand">Expand to see full table
      <svg width="33" height="18" viewBox="0 0 33 18" aria-hidden="true">
        <rect x="0.5" y="0.5" width="32" height="17" fill="none" stroke="#111"/>
        <line x1="0" y1="6" x2="33" y2="6" stroke="#111"/>
        <line x1="0" y1="12" x2="33" y2="12" stroke="#111"/>
        <line x1="11" y1="0" x2="11" y2="18" stroke="#111"/>
        <line x1="22" y1="0" x2="22" y2="18" stroke="#111"/>
      </svg>
    </div>
  </section>

  <div class="rule" style="top:268px"></div>
  <div class="chart-title" style="top:284px">Spread v/s supply</div>
  <svg class="plot" style="top:300px" width="320" height="175" viewBox="0 300 320 175" aria-label="Bubble chart of spread versus supply">
    <circle cx="57" cy="405" r="31" fill="var(--orange)"/>
    <circle cx="136" cy="362" r="54" fill="var(--green)"/>
    <circle cx="105" cy="443" r="23" fill="var(--blue-light)"/>
    <circle cx="248" cy="404" r="57" fill="var(--blue)"/>
    <g fill="#fff" font-size="14" text-anchor="middle">
      <text x="58" y="410">12%</text>
      <text x="137" y="367">45%</text>
      <text x="104" y="448">11%</text>
      <text x="248" y="410">32%</text>
    </g>
  </svg>

  <div class="rule" style="top:486px"></div>
  <div class="chart-title" style="top:497px">Spreads across time</div>
  <svg class="plot" style="top:515px" width="320" height="145" viewBox="0 515 320 145" aria-label="Line chart of spreads across time">
    <polyline points="11,522 11,655 301,655" fill="none" stroke="#9a9a9a" stroke-width="1.5"/>
    <polyline points="25,623 85,592 134,632 192,557 241,613 293,582" fill="none" stroke="#b3b3b3" stroke-width="2"/>
    <circle cx="85" cy="592" r="8" fill="var(--green)"/>
    <circle cx="134" cy="632" r="8" fill="#1b75bc"/>
    <circle cx="192" cy="557" r="8" fill="var(--orange-soft)"/>
    <circle cx="241" cy="613" r="8" fill="var(--grey-dot)"/>
  </svg>

  <footer class="footer">
    <div>About us | FAQ | Contacts</div>
    <div>GasSpread 2014</div>
  </footer>
</div>
</body>
</html>
```